KRT,LLC

I need a flyer that has my company Logo on it as well as my book cover on it. I need for the flyer to read: "Ashes Under the Bridge" ~ A story of Money,Murder,Sex and family ties in the heart of the city. Read along as Curtis J. Hollow masterfully paint this Wilmington,Delaware tale like no other~The "T.K.V boys" clash in a rain of bullets against North sides own "Zinga boys."
At $14.99 you can own your own copy of "Ashes Under the Bridge."
Contact Curt Hollow @ 302-555-0147 to purchase your paper back copy.
OR
Visit:www.krtllcbooks.example
www.ashezunderthebridge.example
ashesunderthebridge24@mailbox.example
To purchase your order directly off line.
We accept paxo,CoinLeaf and debit cards for those individuals who wish to order on-line!

```html
<!DOCTYPE html>
<html lang="en">
<head>
<meta charset="utf-8">
<title>Ashes Under the Bridge – Flyer</title>
<link rel="stylesheet" href="https://fonts.googleapis.com/css2?family=Creepster&family=Alfa+Slab+One&family=Open+Sans:wght@400;600;700&display=swap">
<style>
  :root {
    --backdrop: #7b1317;
    --paper: #ffffff;
    --blood: #a3141b;
    --alert-red: #e01b24;
    --ink: #1a1a1a;
    --royal: #2f3e9e;
    --royal-deep: #1e2a78;
    --navy-bar: #1b2060;
    --mist: #dfe3ea;
    --gold: #f6c400;
    --star: #1c1f4a;
  }
  * { box-sizing: border-box; margin: 0; padding: 0; }
  html, body { width: 1200px; height: 1000px; overflow: hidden; }
  body {
    background: var(--backdrop);
    font-family: "Open Sans", Arial, sans-serif;
    color: var(--ink);
    position: relative;
  }
  .flyer {
    position: absolute; left: 250px; top: 25px;
    width: 700px; height: 950px;
    background: var(--paper);
    overflow: hidden;
    box-shadow: 0 6px 18px rgba(0,0,0,.35);
  }
  .title-main {
    position: absolute; top: 6px; left: 0; width: 100%;
    text-align: center;
    font-family: "Creepster", "Open Sans", cursive;
    font-size: 158px; line-height: 1;
    color: var(--blood);
    letter-spacing: 6px;
  }
  .title-sub {
    position: absolute; top: 172px; left: 0; width: 100%;
    text-align: center;
    font-family: "Alfa Slab One", Georgia, serif;
    font-size: 40px; line-height: 1;
    color: #8a1a1f;
    letter-spacing: 1px;
  }
  .title-sub .accent { color: var(--royal); }
  .tagline {
    position: absolute; top: 226px; left: 0; width: 100%;
    text-align: center; font-size: 20px; font-weight: 400;
  }
  .tagline strong { color: var(--alert-red); font-weight: 700; }
  .blurb {
    position: absolute; top: 256px; left: 75px; width: 550px;
    text-align: center; font-size: 14.5px; line-height: 1.35;
  }
  .rivals {
    position: absolute; top: 306px; left: 0; width: 100%;
    text-align: center; font-size: 22px;
  }
  .collage {
    position: absolute; top: 342px; left: 0; width: 700px; height: 370px;
    background:
      radial-gradient(ellipse at 12% 40%, #c9a89e 0%, transparent 45%),
      radial-gradient(ellipse at 90% 35%, #7d8a6c 0%, transparent 45%),
      radial-gradient(ellipse at 85% 80%, #8d8d8f 0%, transparent 40%),
      radial-gradient(ellipse at 15% 85%, #b25a8e 0%, transparent 35%),
      linear-gradient(180deg, #d7d2cf 0%, #bdb6b3 60%, rgba(255,255,255,0) 100%);
    -webkit-mask-image: linear-gradient(180deg, #000 70%, transparent 100%);
            mask-image: linear-gradient(180deg, #000 70%, transparent 100%);
  }
  .book-cover {
    position: absolute; top: 372px; left: 175px; width: 285px; height: 195px;
    background: linear-gradient(90deg, #2c3aa0 0%, #3545b0 48%, #1e2a78 50%, #3c4ab5 52%, #4d5ac0 100%);
    box-shadow: 2px 4px 10px rgba(0,0,0,.4);
  }
  .price-burst { position: absolute; top: 346px; left: 420px; width: 78px; height: 78px; }
  .crowd-photo {
    position: absolute; top: 580px; left: 240px; width: 170px; height: 90px;
    background: linear-gradient(180deg, #8c96a8, #5a5f6a);
    opacity: .8;
  }
  .wave { position: absolute; left: 0; top: 680px; width: 700px; height: 270px; }
  .offer {
    position: absolute; top: 696px; left: 0; width: 100%;
    text-align: center; font-size: 19px;
  }
  .offer b { font-size: 21px; }
  .offer-title {
    position: absolute; top: 722px; left: 0; width: 100%;
    text-align: center; font-size: 29px; font-weight: 700;
    color: var(--alert-red);
  }
  .contact {
    position: absolute; top: 756px; left: 0; width: 100%;
    text-align: center; font-size: 31px;
  }
  .contact b { font-weight: 700; }
  .contact-note {
    position: absolute; top: 800px; left: 0; width: 100%;
    text-align: center; font-size: 15px;
  }
  .or {
    position: absolute; top: 821px; left: 0; width: 100%;
    text-align: center; font-size: 15px; color: var(--ink);
  }
  .brand {
    position: absolute; top: 848px; left: 16px;
    display: flex; align-items: center; gap: 6px;
  }
  .brand-dot {
    width: 20px; height: 20px; border-radius: 50%;
    background: #fff;
  }
  .brand-name {
    font-family: "Open Sans", Arial, sans-serif;
    font-size: 15px; font-weight: 700; color: #fff;
  }
  .web-links {
    position: absolute; top: 846px; left: 150px; width: 520px;
    display: flex; justify-content: space-between;
    font-size: 13px; color: #fff;
  }
  .web-email {
    position: absolute; top: 863px; left: 0; width: 100%;
    text-align: center; font-size: 13px; color: #fff;
  }
  .web-note {
    position: absolute; top: 880px; left: 0; width: 100%;
    text-align: center; font-size: 13px; color: #fff;
  }
  .payment-bar {
    position: absolute; left: 0; bottom: 0; width: 100%; height: 34px;
    background: var(--navy-bar);
    color: #fff; font-size: 13px;
    display: flex; align-items: center; justify-content: center;
  }
</style>
</head>
<body>
  <main class="flyer">
    <h1 class="title-main">ASHES</h1>
    <p class="title-sub">UNDER THE <span class="accent">BRIDGE</span></p>
    <p class="tagline">A story of <strong>Money, Murder, Sex and family</strong> ties in the heart of the city.</p>
    <p class="blurb">Read along as Curtis J. Hollow masterfully paint this Wilmington, Delaware tale like no other~The "T.K.V boys" clash in a rain of bullets against North sides own</p>
    <p class="rivals">"Zinga boys."</p>

    <div class="collage" role="img" aria-label="Collage of street photographs from the neighbourhood: characters, cash and street signs"></div>
    <div class="book-cover" role="img" aria-label="Book cover of Ashes Under the Bridge, back, spine and front"></div>
    <div class="crowd-photo" role="img" aria-label="Photograph of a group standing outside"></div>

    <svg class="price-burst" viewBox="0 0 100 100" aria-label="Buy $14.99 only">
      <polygon fill="var(--star)" points="50,0 59,18 78,8 76,29 97,28 85,45 100,58 80,64 88,84 67,80 62,100 50,85 38,100 33,80 12,84 20,64 0,58 15,45 3,28 24,29 22,8 41,18"/>
      <text x="50" y="40" text-anchor="middle" font-family="Open Sans, sans-serif" font-weight="700" font-size="15" fill="var(--gold)">Buy</text>
      <text x="50" y="60" text-anchor="middle" font-family="Open Sans, sans-serif" font-weight="700" font-size="17" fill="var(--alert-red)">$14.99</text>
      <text x="50" y="76" text-anchor="middle" font-family="Open Sans, sans-serif" font-weight="700" font-size="12" fill="#fff">Only</text>
    </svg>

    <svg class="wave" viewBox="0 0 700 270" preserveAspectRatio="none" aria-hidden="true">
      <defs>
        <linearGradient id="mistFade" x1="0" y1="0" x2="0" y2="1">
          <stop offset="0" stop-color="#ffffff" stop-opacity="0"/>
          <stop offset="1" stop-color="#dfe3ea"/>
        </linearGradient>
        <linearGradient id="royalBand" x1="0" y1="0" x2="0" y2="1">
          <stop offset="0" stop-color="#3a4bb0"/>
          <stop offset="1" stop-color="#23308a"/>
        </linearGradient>
      </defs>
      <rect x="0" y="0" width="700" height="270" fill="url(#mistFade)"/>
      <path d="M0 105 Q60 155 200 160 L500 160 Q640 155 700 100 L700 270 L0 270 Z" fill="url(#royalBand)"/>
    </svg>

    <p class="offer">At <b>$14.99</b> you can own your own copy of</p>
    <p class="offer-title">"Ashes Under the Bridge."</p>
    <p class="contact">Contact Curt Hollow @ <b>302-555-0147</b></p>
    <p class="contact-note">to purchase your paper back copy.</p>
    <p class="or">OR</p>

    <div class="brand">
      <span class="brand-dot"></span>
      <span class="brand-name">KRT,LLC</span>
    </div>

    <div class="web-links">
      <span>Visit: www.krtllcbooks.example</span>
      <span>www.ashezunderthebridge.example</span>
    </div>
    <p class="web-email">ashesunderthebridge24@mailbox.example</p>
    <p class="web-note">To purchase your order directly off line.</p>

    <footer class="payment-bar">We accept paxo, CoinLeaf and debit cards for those individuals who wish to order on-line!</footer>
  </main>
</body>
</html>
```